Airport Advertising Brochure

I need a flyer put together asap! Previous example included. Would like something clean and updated. New logo and updated company name. I would like this designed in Pages or Illustrator so I can update content when needed. Website: pagelantern.com

Target Market(s)

Authors. This page has some good content about what we do: https://www.pagelantern.com/terminalpromos/

Industry/Entity Type

Airport

Font styles to use
Serif
Sans Serif

Requirements
Must have
• Clean, modern design.

```html
<!DOCTYPE html>
<html lang="en">
<head>
<meta charset="utf-8">
<title>PageLantern – Book Marketing Flyer</title>
<link rel="stylesheet" href="https://fonts.googleapis.com/css2?family=Playfair+Display:wght@400&family=Open+Sans:wght@400;600;700&display=swap">
<style>
  :root {
    --yellow: #f7c600;
    --yellow-deep: #e8a900;
    --ink: #1c1c1c;
    --footer: #111111;
    --paper: #ffffff;
    --rule: #3a3a3a;
    --shelf-dark: #3b2418;
    --shelf-mid: #7a4a2c;
    --shelf-warm: #b8773f;
  }
  * { margin: 0; padding: 0; box-sizing: border-box; }
  html, body { width: 849px; height: 1200px; overflow: hidden; background: var(--paper); }
  .flyer {
    position: relative;
    width: 849px; height: 1200px;
    overflow: hidden;
    background: var(--paper);
    font-family: "Open Sans", Arial, sans-serif;
    color: var(--ink);
  }
  .hero-photo {
    position: absolute; left: 0; top: 0;
    width: 849px; height: 620px;
    background:
      linear-gradient(100deg, rgba(20,10,5,.55) 0%, rgba(0,0,0,0) 45%),
      linear-gradient(180deg, var(--shelf-dark) 0%, var(--shelf-mid) 40%, var(--shelf-warm) 70%, var(--shelf-mid) 100%);
  }
  .hero-edge { position: absolute; left: 0; top: 500px; width: 849px; height: 200px; }
  .title-accent {
    position: absolute; left: 0; top: 660px;
    width: 52px; height: 62px;
    background: var(--yellow);
  }
  .headline {
    position: absolute; left: 70px; top: 648px;
    font-family: "Playfair Display", Georgia, serif;
    font-weight: 400; font-size: 70px; line-height: 1;
    color: var(--ink);
  }
  .headline-rule {
    position: absolute; left: 70px; top: 740px;
    width: 700px; height: 2px; background: var(--rule);
  }
  .service-list {
    position: absolute; left: 48px; top: 762px;
    width: 500px; list-style: none;
  }
  .service-list li {
    position: relative;
    padding-left: 28px;
    font-weight: 700; font-size: 27px; line-height: 1.22;
    margin-bottom: 16px;
  }
  .service-list li::before {
    content: "";
    position: absolute; left: 2px; top: 12px;
    width: 11px; height: 11px;
    background: var(--yellow);
    transform: rotate(45deg);
  }
  .brand {
    position: absolute; left: 560px; top: 960px;
    display: flex; align-items: center; gap: 14px;
  }
  .brand-mark { width: 30px; height: 30px; background: var(--yellow); }
  .brand-name {
    font-family: "Open Sans", Arial, sans-serif;
    font-weight: 600; font-size: 40px; color: var(--ink);
  }
  .footer-shape { position: absolute; left: 0; top: 1010px; width: 849px; height: 190px; }
  .address {
    position: absolute; left: 40px; top: 1055px;
    color: var(--paper); font-size: 20px; line-height: 1.3;
  }
  .address .company { font-weight: 600; display: flex; align-items: center; gap: 8px; }
  .address .street { padding-left: 26px; }
  .contact-row {
    position: absolute; left: 22px; top: 1148px;
    display: flex; gap: 30px;
    color: var(--paper); font-size: 19px;
  }
  .contact-item { display: flex; align-items: center; gap: 9px; }
  .contact-item svg { flex: none; }
</style>
</head>
<body>
<main class="flyer">
  <div class="hero-photo" role="img" aria-label="Photograph of a curved library bookshelf filled with colourful books"></div>

  <svg class="hero-edge" viewBox="0 0 849 200" aria-hidden="true">
    <path d="M0 75 C 250 150, 560 150, 849 70 L849 200 L0 200 Z" fill="var(--yellow)"/>
    <path d="M0 100 C 260 175, 560 165, 849 95 L849 200 L0 200 Z" fill="var(--paper)"/>
  </svg>

  <div class="title-accent"></div>
  <h1 class="headline">Book Marketing</h1>
  <div class="headline-rule"></div>

  <ul class="service-list">
    <li>Comprehensive Window Display, Front Table Placement, and Business Center Pockets.</li>
    <li>45 Airports</li>
    <li>2 Train Stations</li>
    <li>80 Bookstores</li>
  </ul>

  <div class="brand">
    <span class="brand-mark"></span>
    <span class="brand-name">PageLantern</span>
  </div>

  <svg class="footer-shape" viewBox="0 0 849 190" aria-hidden="true">
    <path d="M0 20 C 300 50, 600 10, 849 0 L849 190 L0 190 Z" fill="var(--yellow)"/>
    <path d="M0 32 C 300 62, 600 24, 849 14 L849 190 L0 190 Z" fill="var(--footer)"/>
  </svg>

  <div class="address">
    <div class="company">
      <svg width="18" height="22" viewBox="0 0 18 22" aria-hidden="true"><path d="M9 0a9 9 0 0 0-9 9c0 7 9 13 9 13s9-6 9-13a9 9 0 0 0-9-9z" fill="var(--yellow)"/><circle cx="9" cy="9" r="3.4" fill="var(--footer)"/></svg>
      PageLantern
    </div>
    <div class="street">47 Harbor Ave</div>
    <div class="street">Brooklyn NY 11205</div>
  </div>

  <div class="contact-row">
    <div class="contact-item">
      <svg width="20" height="20" viewBox="0 0 24 24" aria-hidden="true"><path d="M6.6 10.8a15 15 0 0 0 6.6 6.6l2.2-2.2a1 1 0 0 1 1-.25 11.4 11.4 0 0 0 3.6.57 1 1 0 0 1 1 1V20a1 1 0 0 1-1 1A17 17 0 0 1 3 4a1 1 0 0 1 1-1h3.5a1 1 0 0 1 1 1c0 1.25.2 2.45.57 3.57a1 1 0 0 1-.25 1z" fill="var(--yellow)"/></svg>
      +1 (646) 555-0172
    </div>
    <div class="contact-item">
      <svg width="24" height="18" viewBox="0 0 24 18" aria-hidden="true"><rect width="24" height="18" rx="2" fill="var(--yellow)"/><path d="M1 2l11 8 11-8" stroke="var(--footer)" stroke-width="2" fill="none"/></svg>
      hello@pagelantern.com
    </div>
    <div class="contact-item">
      <svg width="20" height="20" viewBox="0 0 24 24" aria-hidden="true"><circle cx="12" cy="12" r="11" fill="var(--yellow)"/><path d="M1 12h22M12 1c3 3 4.5 7 4.5 11S15 20 12 23M12 1C9 4 7.5 8 7.5 12S9 20 12 23" stroke="var(--footer)" stroke-width="1.6" fill="none"/></svg>
      www.pagelantern.com
    </div>
  </div>
</main>
</body>
</html>
```